A layout of a webpage for oil trade platform

I would like to have a desgin of one page webpage (with section scrollling dowin) that woulf present the new product i.e. oil trade platform for wholesale buyers and sellers.
Layout should consist of the sections similar to the given at: https://klinika.pewnywybor.pl/system-zarzadzania-wizytami
However oil industy require more colors and more photo stories than here for doctor.
I. I woul imagine at first below menu a slider with brueg information about the product and its advantages with "more" button next to the prict screen of our platform on different displays (PC and mobile).
II. Bellow the slider I would imagine icons correspoing to the advantages of that plaftorm:
1. Purchase/sale process automation 24/7
2. Access to the best deals
3. Electronic offerings and orderings
4. Transaction status monitoring
5. Data and transaction security
II A) (optional):
In near future we would like to prepare a short video presenation. Hence please prepare a place to display that element here.
At the moment alternatvily please prepare a How it works section that would explan the platform operating process
III. Next secion is about benefits for Oil Purchaser
It can be done either by icons of by text and corresponding grahip for while section.
Benefits:
- Access to cheaper oil
- Convenience of online orders
- Possibility to compare prices on the market
- Transaction history
- Order status monitoring
- Seccurity and transparency of purchase
IV. Next seciont is about benefits for Oil Seller
Benefits:
- New sale channel
- Attracting new clients
- More oil sold
- Transaction security
- Possibility to integrate with distribution infrastructure and logistits for more efficient automation.
V. Contact form
VI. Footer
I would need a layout that that will correspond to the very dynamic logo but I would expect also a clean form, smoth and modern. It has to be proffessional layout with more corporate character.
It can use a paralax features if needed.

```html
<!DOCTYPE html>
<html lang="en">
<head>
<meta charset="utf-8">
<title>Crudeon Contest</title>
<link href="https://fonts.googleapis.com/css2?family=Lato:wght@400;700&family=Montserrat:wght@400;500;600;700&family=Playfair+Display:ital@1&display=swap" rel="stylesheet">
<style>
:root{
  --board-dark:#1e2124;
  --board-mid:#3b3f42;
  --accent-blue:#1a8fd6;
  --brush-white:#f4f4f4;
  --orange:#f2571b;
  --ink:#222428;
  --muted:#8a8d91;
  --section-light:#f6f6f6;
  --sea-top:#8fb3b7;
  --sea-bottom:#2e4a6e;
  --video-dark:#1b1b1c;
}
*{margin:0;padding:0;box-sizing:border-box}
html,body{width:1200px;height:800px;overflow:hidden;background:var(--board-dark)}
.board{position:relative;width:1200px;height:800px;overflow:hidden;font-family:"Lato",sans-serif}
.board-backdrop{position:absolute;inset:0;background:radial-gradient(ellipse at 20% 40%,#55524c 0%,#34363a 40%,var(--board-dark) 80%)}
.board-title{position:absolute;left:8px;top:104px;font-size:52px;font-weight:400;color:#fff;letter-spacing:.2px}
.point{position:absolute;left:0;height:54px;width:425px;background:var(--brush-white);clip-path:polygon(0 14%,30% 6%,70% 12%,100% 4%,98% 88%,60% 96%,25% 90%,0 94%)}
.point-text{position:absolute;left:2px;font-size:32px;color:var(--accent-blue);white-space:nowrap}
.feedback{position:absolute;left:22px;top:643px;width:351px;height:91px;background:rgba(90,92,95,.85);color:#fff;text-align:center;font-size:32px;line-height:27px;padding-top:16px}

.site{position:absolute;left:427px;top:118px;width:736px;height:682px;background:#fff;overflow:hidden}
.hero{position:absolute;left:0;top:0;width:736px;height:329px;background:linear-gradient(180deg,var(--sea-top) 0%,#a8c2c2 55%,#4d6a84 72%,var(--sea-bottom) 100%)}
.brand{position:absolute;left:140px;top:26px;display:flex;align-items:center;gap:6px;font-family:"Montserrat",sans-serif;font-size:13px;font-weight:500;color:var(--ink)}
.brand-dot{width:10px;height:10px;border-radius:50%;background:var(--orange)}
.nav{position:absolute;left:340px;top:34px;display:flex;gap:15px;font-family:"Montserrat",sans-serif;font-size:5.5px;font-weight:700;color:#fff;letter-spacing:.4px}
.nav .active{position:relative}
.nav .active::after{content:"";position:absolute;left:3px;top:10px;width:11px;border-top:2px dotted var(--orange)}
.hero-title{position:absolute;left:172px;top:114px;font-family:"Montserrat",sans-serif;font-weight:700;font-size:22px;color:#fff;letter-spacing:1px}
.hero-title span{color:var(--orange)}
.hero-desc{position:absolute;left:185px;top:141px;font-family:"Playfair Display",serif;font-style:italic;font-size:8px;color:#2d3a44}
.hero-desc span{color:var(--orange)}
.features{position:absolute;left:193px;top:156px;list-style:none;font-family:"Playfair Display",serif;font-style:italic;font-size:12px;line-height:15.5px;color:#fff}
.features li::before{content:"";display:inline-block;width:4px;height:4px;border-radius:50%;background:var(--orange);margin:0 5px 2px -9px}
.see-more{position:absolute;left:251px;top:211px;width:51px;height:20px;background:var(--orange);color:#fff;font-family:"Montserrat",sans-serif;font-size:5px;font-weight:600;display:flex;align-items:center;justify-content:center}
.slider-dots{position:absolute;left:358px;top:313px;display:flex;gap:3px}
.slider-dots i{width:6px;height:6px;border-radius:50%;background:var(--orange)}
.slider-dots i.on{background:#fff}

.advantages{position:absolute;left:0;top:329px;width:736px;height:204px;background:var(--section-light);text-align:center}
.eyebrow{position:absolute;left:0;right:0;top:34px;font-family:"Montserrat",sans-serif;font-size:5.5px;color:#555;letter-spacing:.5px}
.section-title{position:absolute;left:0;right:0;top:49px;font-family:"Montserrat",sans-serif;font-size:14.5px;font-weight:600;color:var(--ink);letter-spacing:.6px}
.divider{position:absolute;left:325px;top:68px}
.adv{position:absolute;top:97px;width:110px;margin-left:-55px}
.adv svg{display:block;margin:0 auto}
.adv h3{margin-top:7px;font-family:"Montserrat",sans-serif;font-size:4.6px;font-weight:700;color:var(--ink)}
.adv p{margin-top:8px;font-family:"Montserrat",sans-serif;font-size:4.6px;line-height:8px;color:var(--muted);padding:0 14px}

.video{position:absolute;left:0;top:536px;width:736px;height:146px;background:var(--video-dark);border-top:4px solid #4a4a4a}
.video-photo{position:absolute;left:80px;top:4px;width:260px;height:142px;background:radial-gradient(ellipse at 45% 45%,#6b5d54 0%,#3b3432 50%,var(--video-dark) 85%)}
.video-title{position:absolute;left:240px;top:100px;font-family:"Montserrat",sans-serif;font-size:29px;font-weight:700;color:#fff}
</style>
</head>
<body>
<main class="board">
  <div class="board-backdrop" role="img" aria-label="Blurred photo of an industrial workspace in dark tones"></div>

  <h1 class="board-title">Crudeon Contest</h1>

  <div class="point" style="top:328px"></div>
  <p class="point-text" style="top:329px">&gt;Colors Based on Logo colors</p>
  <div class="point" style="top:426px"></div>
  <p class="point-text" style="top:426px">&gt;Design follows website map</p>
  <div class="point" style="top:518px"></div>
  <p class="point-text" style="top:519px;left:4px">&gt;High-Res Image attached</p>

  <div class="feedback">Please Don’t Forget to<br>Give me Feedback</div>

  <section class="site">
    <header class="hero" role="img" aria-label="Photo of an offshore oil platform standing in the sea">
      <div class="brand"><span class="brand-dot"></span>Crudeon</div>
      <nav class="nav">
        <span class="active">HOME</span><span>PRODUCT</span><span>ABOUT US</span><span>CONTACT US</span><span>SERVICES</span><span>TEAM</span>
        <svg width="7" height="7" viewBox="0 0 10 10"><path d="M0 1h2l1.5 5h5L10 2.5H3" fill="none" stroke="#fff" stroke-width="1.3"/><circle cx="4" cy="8.5" r="1" fill="#fff"/><circle cx="8" cy="8.5" r="1" fill="#fff"/></svg>
        <svg width="7" height="7" viewBox="0 0 10 10"><circle cx="4" cy="4" r="3" fill="none" stroke="#fff" stroke-width="1.4"/><path d="M6.3 6.3 9.3 9.3" stroke="#fff" stroke-width="1.4"/></svg>
      </nav>
      <h2 class="hero-title">PRODUCT NAME<span>.</span></h2>
      <p class="hero-desc">write an attractive description about your <span>PRODUCT</span></p>
      <ul class="features"><li>Feature 1</li><li>Feature 2</li><li>Feature 3</li></ul>
      <a class="see-more">SEE MORE</a>
      <div class="slider-dots"><i></i><i></i><i class="on"></i><i></i><i></i></div>
    </header>

    <section class="advantages">
      <p class="eyebrow">Why us ?</p>
      <h2 class="section-title">OUR PLATFORM ADVANTAGES</h2>
      <svg class="divider" width="86" height="8" viewBox="0 0 86 8"><path d="M0 4h36M50 4h36" stroke="#ccc" stroke-width=".8"/><path d="M40 1l6 6M46 1l-6 6" stroke="#333" stroke-width="1"/></svg>

      <div class="adv" style="left:181px">
        <svg width="14" height="14" viewBox="0 0 14 14"><circle cx="7" cy="7" r="6" fill="none" stroke="var(--orange)" stroke-width="1"/><path d="M7 3.5V7h3" fill="none" stroke="var(--orange)" stroke-width="1"/></svg>
        <h3>PURCHASE/SALE PROCESS AUTOMATION 24/7</h3>
        <p>Fast deals for buyers and sellers daily.</p>
      </div>
      <div class="adv" style="left:275px">
        <svg width="14" height="14" viewBox="0 0 14 14"><circle cx="7" cy="5" r="4" fill="none" stroke="var(--orange)" stroke-width="1"/><path d="M4.5 8 3 13l4-2 4 2-1.5-5" fill="none" stroke="var(--orange)" stroke-width="1"/></svg>
        <h3>ACCESS TO THE BEST DEALS</h3>
        <p>Compare market offers and pick the best.</p>
      </div>
      <div class="adv" style="left:365px">
        <svg width="14" height="14" viewBox="0 0 14 14"><rect x="4" y="1" width="6" height="12" rx="1" fill="none" stroke="var(--orange)" stroke-width="1"/><path d="M6 11h2" stroke="var(--orange)" stroke-width="1"/></svg>
        <h3>ELECTRONIC OFFERINGS AND ORDERINGS</h3>
        <p>Place offers and orders online in minutes.</p>
      </div>
      <div class="adv" style="left:461px">
        <svg width="14" height="14" viewBox="0 0 14 14"><rect x="1" y="2" width="12" height="8" fill="none" stroke="var(--orange)" stroke-width="1"/><path d="M5 12.5h4M7 10v2.5" stroke="var(--orange)" stroke-width="1"/></svg>
        <h3>TRANSACTION STATUS MONITORING</h3>
        <p>Follow each order from offer to delivery.</p>
      </div>
      <div class="adv" style="left:559px">
        <svg width="14" height="14" viewBox="0 0 14 14"><path d="M7 1l5 2v4c0 3-2.5 5-5 6-2.5-1-5-3-5-6V3z" fill="none" stroke="var(--orange)" stroke-width="1"/></svg>
        <h3>DATA AND TRANSACTION SECURITY</h3>
        <p>Your data and payments stay fully protected.</p>
      </div>
    </section>

    <section class="video">
      <div class="video-photo" role="img" aria-label="Photo of a presenter for the video section"></div>
      <h2 class="video-title">WATCH OUR VIDEO</h2>
    </section>
  </section>
</main>
</body>
</html>
```